Billboard Design for Modern Dispensary

Hello!
We need a eye-catching 12' x 24' billboard designed for a very successful, modern cannabis dispensary on the Oregon coast, United States. Because of rules, we cannot have any marijuana leafs or other cannabis related images (flower, joints, smoke, etc). We can use the words "Shop" or "Dispensary" - we cannot use the words "cannabis", "marijuana".

Some ideas we had are 3 words stacked on left or center of billboard - maybe across bottom we have horizontal logo and the following words - “South of bridge in Tidecrest Bay”
Another idea is to have a small bubble in bottom/top corner with image of our dog (face only) - with some words around it - like "BONUS Shop Dog" or "Cute Shop Dog" or "Best Shop Dog" or "Friendly Staff"

here's some 3 word examples:
ENJOY
YOUR
TRIP

or

FEEL
GOOD
JUST
AHEAD

or

GOOD
VIBES
ONLY

or

GOOD
TIMES
CHILL
VIBES

I have attached our logo. I have also included a stacked logo version (vertical, not horizontal). the formats are .EPS and .PDF - the logos were created in Affinity Design 2.x.

Our website is coralnook.net if you want to see more images, etc about our dispensary.

Artwork Requirements:
The billboard is 12' tall x 25' wide
The artwork needs to be 1”=1’ @ 300dpi
Please add 6” of bleed all around so your total artwork is 13”x26”
Final deliverable should be .Ai file.

Font styles to use
Sans Serif

Colors
0054AA
0677BA
7BADD7
CADEEF
E8F1F8

Requirements
Nice to have
• See the project description - we included some ideas to consider.
Should not have
• No cannabis images, like flower, cannabis leaves, paraphenlia, cartridges, joints, etc.

```html
<!DOCTYPE html>
<html lang="en">
<head>
<meta charset="utf-8">
<title>Coral Nook Billboard</title>
<link href="https://fonts.googleapis.com/css2?family=Oswald:wght@700&family=Poppins:wght@400;600;700&family=Questrial&display=swap" rel="stylesheet">
<style>
  :root {
    --stage: #5a5a5a;
    --paper: #efefef;
    --paper-shade: #e4e4e4;
    --ocean: #1d68a0;
    --sky: #449dd6;
    --ink: #111111;
    --white: #ffffff;
    --dog-light: #dcc08e;
    --dog-dark: #b58f5a;
  }
  html, body {
    margin: 0;
    padding: 0;
    width: 955px;
    height: 1200px;
    overflow: hidden;
    background: var(--stage);
  }
  .canvas {
    position: relative;
    width: 955px;
    height: 1200px;
  }
  .billboard {
    position: absolute;
    left: 37px;
    top: 380px;
    width: 880px;
    height: 439px;
    box-shadow: 0 10px 28px rgba(0,0,0,0.45);
  }
  .billboard svg { display: block; }
  .brand-name {
    font-family: "Questrial", sans-serif;
    fill: var(--sky);
  }
  .brand-place {
    font-family: "Questrial", sans-serif;
    fill: var(--ink);
    letter-spacing: 7px;
  }
  .headline {
    font-family: "Oswald", sans-serif;
    font-weight: 700;
    fill: var(--white);
  }
  .tagline {
    font-family: "Poppins", sans-serif;
    font-weight: 400;
    fill: var(--ink);
  }
  .tagline .tagline-strong { font-weight: 700; }
  .dog-label {
    font-family: "Poppins", sans-serif;
    font-weight: 600;
    fill: var(--ocean);
  }
</style>
</head>
<body>
<div class="canvas">
  <div class="billboard">
    <svg width="880" height="439" viewBox="0 0 880 439" xmlns="http://www.w3.org/2000/svg">
      <defs>
        <linearGradient id="paperFade" x1="0" y1="0" x2="1" y2="1">
          <stop offset="0" stop-color="var(--paper)"/>
          <stop offset="1" stop-color="var(--paper-shade)"/>
        </linearGradient>
        <linearGradient id="dogTone" x1="0" y1="0" x2="0" y2="1">
          <stop offset="0" stop-color="var(--dog-light)"/>
          <stop offset="1" stop-color="var(--dog-dark)"/>
        </linearGradient>
      </defs>

      <!-- upper panel -->
      <rect class="panel-top" width="880" height="439" fill="url(#paperFade)"/>

      <!-- torn light edge -->
      <path class="torn-edge" fill="var(--sky)"
        d="M0 200 L22 196 L40 199 L58 193 L75 197 L96 194 L110 198 L128 191 L150 196 L170 194 L188 198 L205 192 L226 195 L248 193 L266 197 L285 190 L302 195 L322 193 L340 198 L360 192 L380 196 L398 193 L418 197 L440 191 L460 196 L478 194 L498 198 L515 192 L536 196 L556 193 L575 197 L596 191 L615 196 L636 194 L655 198 L676 192 L696 196 L716 193 L735 197 L756 191 L776 196 L796 194 L818 198 L838 192 L860 195 L880 190 L880 439 L0 439 Z"/>

      <!-- torn dark band -->
      <path class="band" fill="var(--ocean)"
        d="M0 217 L18 212 L36 215 L54 209 L72 214 L92 211 L112 216 L130 210 L152 214 L172 211 L190 215 L210 209 L232 213 L252 210 L272 214 L292 208 L312 213 L332 211 L352 215 L372 209 L392 213 L414 210 L434 214 L454 208 L474 213 L494 211 L514 215 L534 209 L554 213 L576 210 L596 214 L616 208 L636 213 L656 211 L676 215 L696 209 L716 213 L738 210 L758 214 L778 208 L798 212 L818 209 L840 212 L860 207 L880 210 L880 439 L0 439 Z"/>

      <!-- brand mark -->
      <g class="brand">
        <circle class="brand-dot" cx="132" cy="102" r="62" fill="none" stroke="var(--sky)" stroke-width="7"/>
        <text class="brand-name" x="210" y="127" font-size="66">CORAL NOOK</text>
        <line x1="213" y1="145" x2="272" y2="145" stroke="var(--ink)" stroke-width="1.3"/>
        <text class="brand-place" x="287" y="151" font-size="17">TIDECREST BAY</text>
        <line x1="505" y1="145" x2="564" y2="145" stroke="var(--ink)" stroke-width="1.3"/>
      </g>

      <!-- shop dog -->
      <text class="dog-label" x="773" y="62" font-size="15" text-anchor="middle">BONUS Shop Dog</text>
      <rect class="dog-photo" role="img" aria-label="Photo of the shop dog, a fluffy golden doodle wearing a bandana"
        x="743" y="72" width="72" height="142" rx="30" fill="url(#dogTone)"/>

      <!-- headline -->
      <text class="headline" x="440" y="350" font-size="108" text-anchor="middle" textLength="765" lengthAdjust="spacingAndGlyphs">GOOD VIBES ONLY</text>

      <!-- brush strip and tagline -->
      <path class="brush" fill="var(--white)"
        d="M186 380 L200 377 L420 375 L640 373 L700 374 L690 379 L705 382 L688 386 L700 392 L684 397 L698 404 L680 410 L420 413 L240 415 L205 413 L214 408 L190 405 L205 400 L180 396 L198 391 L176 387 L196 384 Z"/>
      <text class="tagline" x="440" y="404" font-size="25" text-anchor="middle">South of bridge in <tspan class="tagline-strong">Tidecrest Bay</tspan></text>
    </svg>
  </div>
</div>
</body>
</html>
```